GLOW LEAP TWIRL II (POSTCARD DESIGN)

Hello our original designer is no longer on this platform. We want to use design #51936074 with some minor adjustments. I've uploaded the original project 1) change the date on the front of card (keeping the same format) to August 27 with a start time of 2:30 PM.
2) on the front part of the card I want to include a splash graphic that says Back By Popular Demand! 3) replace pictures on the front with the attached photo. make it blend in. 3) Use the same photo on the back of the card.
Let the post card examples serve as template examples and let your creativity flourish! This is time sensitive so get these to me fast! If you're early you may win. thx

```html
<!DOCTYPE html>
<html lang="en">
<head>
<meta charset="utf-8">
<title>Glow Leap Twirl II – Postcard</title>
<link rel="stylesheet" href="https://fonts.googleapis.com/css2?family=Montserrat:ital,wght@0,400;0,500;0,600;0,700;0,800;1,800&family=Orbitron:wght@900&family=Oswald:wght@500&display=swap">
<style>
  :root {
    --page: #b3b3b3;
    --card: #0d0d10;
    --white: #ffffff;
    --pink: #e0197f;
    --pink-soft: #d6297e;
    --teal: #3cc3cc;
    --blue: #1f5bb5;
    --navy: #1b4b9e;
    --yellow: #fcc22d;
    --purple: #5b2b86;
    --violet: #7d3cae;
  }
  * { box-sizing: border-box; margin: 0; padding: 0; }
  html, body { width: 945px; height: 1200px; overflow: hidden; }
  body { background: var(--page); font-family: "Montserrat", sans-serif; position: relative; }

  .card {
    position: absolute; left: 83px; width: 778px; height: 519px;
    background: var(--card); overflow: hidden;
    box-shadow: 0 4px 10px rgba(0,0,0,.45);
  }
  .card--front { top: 57px; background: linear-gradient(135deg, #1c1c20 0%, #0b0b0d 60%); }
  .card--back { top: 624px; background: linear-gradient(160deg, #141018 0%, #0a0a0c 70%); }

  .layer { position: absolute; inset: 0; }

  .presenter {
    position: absolute; left: 26px; color: var(--pink-soft);
    font-weight: 500; font-size: 16.5px; line-height: 22px; letter-spacing: .3px;
  }
  .title-line {
    position: absolute; left: 20px; color: var(--white);
    font-family: "Orbitron", sans-serif; font-weight: 900; font-style: italic;
    letter-spacing: -2px; line-height: 1;
  }
  .title-accent {
    position: absolute; left: 22px;
    font-family: "Orbitron", sans-serif; font-weight: 900; font-style: italic;
    line-height: 1; letter-spacing: -1px;
    background: linear-gradient(90deg, var(--blue) 0%, var(--teal) 42%, var(--teal) 55%, var(--pink) 78%, var(--pink) 100%);
    -webkit-background-clip: text; background-clip: text; color: transparent;
  }

  /* front */
  .card--front .presenter { top: 33px; }
  .card--front .title-line--1 { top: 93px; font-size: 50px; }
  .card--front .title-line--2 { top: 139px; font-size: 50px; }
  .card--front .title-accent { top: 182px; font-size: 90px; }

  .burst { position: absolute; left: 293px; top: 55px; width: 200px; height: 130px; }
  .burst-text {
    position: absolute; left: 293px; top: 95px; width: 200px; text-align: center;
    font-weight: 600; font-size: 14px; line-height: 17px; color: #222;
  }
  .burst-text strong { display: block; color: var(--pink); font-weight: 800; }

  .date-day {
    position: absolute; left: 21px; top: 284px; color: var(--teal);
    font-family: "Oswald", sans-serif; font-weight: 500; font-size: 72px; line-height: 1;
    letter-spacing: -2px;
  }
  .date-month, .date-year {
    position: absolute; left: 86px; color: var(--white); font-weight: 700; line-height: 1;
  }
  .date-month { top: 294px; font-size: 27px; }
  .date-year { top: 322px; font-size: 32px; letter-spacing: 1px; }
  .date-divider { position: absolute; left: 223px; top: 288px; width: 2px; height: 70px; background: var(--pink); }
  .time-label { position: absolute; left: 242px; top: 293px; color: var(--teal); font-weight: 700; font-size: 26px; line-height: 1; }
  .time-value { position: absolute; left: 242px; top: 320px; color: var(--white); font-weight: 700; font-size: 38px; line-height: 1; }

  .venue { position: absolute; left: 47px; top: 364px; color: var(--white); line-height: 1; }
  .venue-name { font-size: 22px; font-weight: 500; letter-spacing: .6px; }
  .venue-city { font-size: 18px; font-weight: 500; margin-top: 2px; letter-spacing: .5px; }
  .venue-pin { position: absolute; left: 20px; top: 367px; width: 16px; height: 22px; }

  .tickets-block {
    position: absolute; left: 19px; top: 430px; width: 120px; height: 76px;
    background: linear-gradient(90deg, var(--navy) 0%, var(--navy) 45%, var(--violet) 100%);
  }
  .tickets-label {
    position: absolute; left: 28px; top: 447px; color: var(--yellow);
    font-weight: 700; font-size: 11px; line-height: 13px;
  }

  .box-office { position: absolute; left: 163px; top: 437px; color: var(--white); font-weight: 500; font-size: 13.5px; line-height: 1; }
  .box-phone { position: absolute; left: 163px; top: 453px; color: var(--pink); font-weight: 800; font-style: italic; font-size: 19px; line-height: 1; }
  .ticket-url {
    position: absolute; left: 161px; top: 478px; width: 232px; height: 26px;
    background: var(--navy); border-radius: 0 13px 13px 0;
    color: var(--white); font-weight: 600; font-size: 14px; letter-spacing: 2.4px;
    line-height: 26px; padding-left: 9px;
  }

  .photo { position: absolute; }
  .photo--portrait {
    left: 478px; top: 48px; width: 240px; height: 471px;
    background: radial-gradient(ellipse at 50% 40%, #eeebe8 0%, #ddd6d0 40%, #b8c3d2 70%, rgba(150,160,185,0) 100%);
    border-radius: 110px 110px 20px 20px;
  }

  /* back */
  .card--back .presenter { top: 20px; }
  .card--back .title-line--1 { top: 69px; font-size: 45px; left: 28px; }
  .card--back .title-line--2 { top: 107px; font-size: 45px; left: 28px; }
  .card--back .title-accent { top: 147px; font-size: 69px; left: 29px; }

  .about {
    position: absolute; left: 30px; top: 219px; width: 425px;
    color: var(--white); font-size: 14.5px; line-height: 17.3px; font-weight: 500;
  }
  .about strong { color: var(--teal); font-weight: 700; }
  .dash-rule { position: absolute; left: 28px; top: 355px; width: 100px; height: 4px; }

  .photo--group {
    left: 36px; top: 373px; width: 302px; height: 113px;
    background: linear-gradient(180deg, #9c2848 0%, #5a1d34 45%, #1e1a22 100%);
    outline: 1.5px solid var(--white);
    transform: skewX(-8deg);
  }
  .photo--dancer {
    left: 470px; top: 58px; width: 308px; height: 461px;
    background: radial-gradient(ellipse at 45% 40%, #4a2a55 0%, #2c1638 45%, rgba(20,12,26,0) 85%);
  }
</style>
</head>
<body>

  <section class="card card--front">
    <svg class="layer" viewBox="0 0 778 519" aria-hidden="true">
      <defs>
        <linearGradient id="frontBand" x1="0" y1="1" x2="1" y2="0">
          <stop offset="0" stop-color="#c0267f"/>
          <stop offset="1" stop-color="#7b2f9a"/>
        </linearGradient>
        <linearGradient id="frontRight" x1="0" y1="0" x2="1" y2="1">
          <stop offset="0" stop-color="#3a2166"/>
          <stop offset="1" stop-color="#5b3496"/>
        </linearGradient>
      </defs>
      <polygon points="650,0 778,0 778,519 425,519" fill="url(#frontRight)"/>
      <polygon points="655,0 700,0 480,519 425,519" fill="url(#frontBand)"/>
    </svg>

    <div class="photo photo--portrait" role="img" aria-label="Photo of the headline dancer in a white blazer, blended into the background"></div>

    <p class="presenter">BRIGHTSTEP PRODUCTIONS PRESENTS<br>NADIA ROSE VALE’S</p>
    <h1 class="title-line title-line--1">GLOW</h1>
    <p class="title-line title-line--2">LEAP</p>
    <p class="title-accent">TWIRL</p>

    <svg class="burst" viewBox="0 0 200 130" aria-hidden="true">
      <polygon fill="#fcc22d" stroke="#3cc3cc" stroke-width="3" stroke-linejoin="miter"
        points="100,3 117,33 148,12 145,42 196,38 160,60 190,82 148,82 158,118 122,98 102,128 88,98 55,118 60,84 6,86 45,62 10,38 55,42 50,12 82,30"/>
    </svg>
    <p class="burst-text">Back By<strong>POPULAR<br>DEMAND!</strong></p>

    <p class="date-day">27</p>
    <p class="date-month">AUGUST</p>
    <p class="date-year">2022</p>
    <span class="date-divider"></span>
    <p class="time-label">START TIME</p>
    <p class="time-value">2:30 PM</p>

    <svg class="venue-pin" viewBox="0 0 16 22" aria-hidden="true">
      <path d="M8 1a6 6 0 0 0-6 6c0 4.5 6 10 6 10s6-5.5 6-10a6 6 0 0 0-6-6z" fill="none" stroke="#e0197f" stroke-width="2"/>
      <circle cx="8" cy="7" r="2" fill="#e0197f"/>
      <line x1="3" y1="20.5" x2="13" y2="20.5" stroke="#e0197f" stroke-width="2"/>
    </svg>
    <div class="venue">
      <p class="venue-name">HARRIET LOWELL THEATRE</p>
      <p class="venue-city">Cedar Hollow, CA</p>
    </div>

    <div class="tickets-block" role="img" aria-label="Ticket graphic in blue and purple"></div>
    <p class="tickets-label">Buy<br>Tickets</p>

    <p class="box-office">Box Office</p>
    <p class="box-phone">(555) 014-SHOW</p>
    <p class="ticket-url">www.tix.example/glw</p>
  </section>

  <section class="card card--back">
    <svg class="layer" viewBox="0 0 778 519" aria-hidden="true">
      <polygon points="715,0 778,0 778,45 425,519 387,519" fill="#e0197f"/>
    </svg>

    <div class="photo photo--dancer" role="img" aria-label="Photo of the headline dancer performing on stage in a sequined purple gown"></div>

    <p class="presenter">BRIGHTSTEP PRODUCTIONS PRESENTS<br>NADIA ROSE VALE’S</p>
    <h2 class="title-line title-line--1">GLOW</h2>
    <p class="title-line title-line--2">LEAP</p>
    <p class="title-accent">TWIRL</p>

    <p class="about"><strong>GLOW, LEAP, TWIRL</strong> showcases the dance styles of urban hip hop. ballet. modern jazz and much much more! Bay Area renowned dancer/choreographer NADIA ROSE VALE headlines this cast of dancers and will amaze you as she takes you on a journey through dance you'll never forget. Join us for an experience that will prove to delight and excite you!</p>

    <svg class="dash-rule" viewBox="0 0 100 4" aria-hidden="true">
      <defs>
        <linearGradient id="dashGrad" x1="0" x2="1">
          <stop offset="0" stop-color="#1f5bb5"/>
          <stop offset=".5" stop-color="#3cc3cc"/>
          <stop offset="1" stop-color="#e0197f"/>
        </linearGradient>
      </defs>
      <line x1="0" y1="2" x2="100" y2="2" stroke="url(#dashGrad)" stroke-width="4" stroke-dasharray="4 2"/>
    </svg>

    <div class="photo photo--group" role="img" aria-label="Group photo of the dance cast in matching show t-shirts on stage"></div>
  </section>

</body>
</html>
```